Book Cover Design Project

We need a book cover for a eBook on internet banking.

This eBook is meant to be an easy to read, practical book to help people understand what internet banking is, the pros and cons and cover the pure 'internet only' banks that have no branches. The intention is to help people to make informed decisions about whether to use internet banking, how to use it safely and explain in detail what 'internet only' banks are and whether they are right for them.

The cover should not look technical so that non-technical people are not scared off by the look. I have uploaded a book cover design that has the style that I am trying to portray, I have also uploaded a front cover that I created but do not think is suitable.

The cover wording layout could be something like
"Internet Banking"
"A practical guide to answer all your questions" or "The ultimate guide to internet banking" or "The Who's What's and How's of Internet Banking"
Authors name : Colin Pettifer

Industry/Entity Type

Internet

```html
<!DOCTYPE html>
<html lang="en">
<head>
<meta charset="utf-8">
<title>The Ultimate Guide: Online Banking</title>
<link rel="stylesheet" href="https://fonts.googleapis.com/css2?family=Audiowide&family=Russo+One&family=Nunito:wght@900&family=Tinos&display=swap">
<style>
  :root {
    --bg-top: #0a2238;
    --bg-mid: #0f4f86;
    --bg-bottom: #1d7fc4;
    --bg-glow: #6fb8e6;
    --red-light: #e8161a;
    --red-dark: #a80808;
    --band-blue: #153b88;
    --pill-white: #f4f4f4;
    --title-red: #b50a0a;
    --online-gold: #ffc400;
    --online-orange: #f08a00;
    --tagline-gold: #ffc21a;
    --tagline-edge: #8a4a00;
    --text-white: #ffffff;
    --author-grey: #e4e8ee;
  }
  html, body {
    margin: 0;
    padding: 0;
    overflow: hidden;
    background: var(--bg-top);
  }
  .cover {
    position: relative;
    width: 831px;
    height: 1200px;
    overflow: hidden;
    background:
      radial-gradient(ellipse 520px 260px at 50% 1120px, var(--bg-glow) 0%, rgba(111,184,230,0) 100%),
      linear-gradient(180deg, var(--bg-top) 0%, #0d3458 35%, var(--bg-mid) 65%, var(--bg-bottom) 100%);
  }
  .title-block {
    position: absolute;
    left: 0;
    top: 0;
    width: 831px;
    height: 420px;
  }
  .subtitle {
    position: absolute;
    left: 0;
    width: 831px;
    top: 418px;
    margin: 0;
    text-align: center;
    font-family: "Tinos", "Times New Roman", serif;
    font-size: 31px;
    font-weight: 400;
    color: var(--text-white);
    text-shadow: 1px 2px 3px rgba(0,0,0,0.7);
  }
  .banknotes {
    position: absolute;
    left: 164px;
    top: 503px;
    width: 513px;
    height: 254px;
    background:
      linear-gradient(135deg, #cfd6c4 0%, #e8b8b0 30%, #f0d9c0 50%, #d9c79a 70%, #c9cfb8 100%);
  }
  .tagline {
    position: absolute;
    left: 0;
    width: 831px;
    top: 850px;
    margin: 0;
    text-align: center;
    font-family: "Audiowide", "Arial Black", sans-serif;
    font-size: 44px;
    line-height: 64px;
    font-weight: 400;
    color: var(--tagline-gold);
    -webkit-text-stroke: 1.5px var(--tagline-edge);
    text-shadow: 2px 3px 3px rgba(0,0,0,0.45);
    letter-spacing: 1px;
  }
  .author {
    position: absolute;
    left: 0;
    width: 831px;
    top: 1086px;
    margin: 0;
    text-align: center;
    font-family: "Tinos", "Times New Roman", serif;
    font-size: 27px;
    color: var(--author-grey);
    text-shadow: 1px 2px 3px rgba(0,0,0,0.55);
  }
</style>
</head>
<body>
<div class="cover">
  <svg class="title-block" viewBox="0 0 831 420" aria-label="The Ultimate Guide: Online Banking">
    <defs>
      <linearGradient id="red-panel" x1="0" y1="0" x2="0" y2="1">
        <stop offset="0" stop-color="var(--red-light)"/>
        <stop offset="1" stop-color="var(--red-dark)"/>
      </linearGradient>
      <linearGradient id="online-fill" x1="0" y1="0" x2="0" y2="1">
        <stop offset="0" stop-color="var(--online-gold)"/>
        <stop offset="1" stop-color="var(--online-orange)"/>
      </linearGradient>
      <linearGradient id="banking-fill" x1="0" y1="0" x2="0" y2="1">
        <stop offset="0" stop-color="#ffffff"/>
        <stop offset="0.5" stop-color="#dfe2e6"/>
        <stop offset="1" stop-color="#9aa0a8"/>
      </linearGradient>
      <linearGradient id="pill-fill" x1="0" y1="0" x2="0" y2="1">
        <stop offset="0" stop-color="#ffffff"/>
        <stop offset="1" stop-color="#d8d8d8"/>
      </linearGradient>
      <clipPath id="panel-clip">
        <rect x="127" y="90" width="576" height="309" rx="16"/>
      </clipPath>
    </defs>
    <rect class="title-panel" x="127" y="90" width="576" height="309" rx="16" fill="url(#red-panel)"/>
    <g clip-path="url(#panel-clip)">
      <path class="title-pill" d="M110 115 H640 a40 40 0 0 1 0 79 H110 Z" fill="url(#pill-fill)" stroke="#7a0000" stroke-width="2"/>
      <rect class="banking-band" x="127" y="266" width="576" height="112" fill="var(--band-blue)"/>
    </g>
    <text x="143" y="174" textLength="520" lengthAdjust="spacingAndGlyphs"
          font-family="Russo One, Arial Black, sans-serif" font-size="48"
          fill="var(--title-red)" stroke="#5a0000" stroke-width="1">THE ULTIMATE GUIDE</text>
    <text x="318" y="252" textLength="194" lengthAdjust="spacingAndGlyphs"
          font-family="Nunito, Arial Rounded MT Bold, sans-serif" font-weight="900" font-size="62"
          fill="url(#online-fill)" stroke="#8a3f00" stroke-width="1">Online</text>
    <text x="200" y="364" textLength="474" lengthAdjust="spacingAndGlyphs"
          font-family="Russo One, Arial Black, sans-serif" font-size="108"
          fill="url(#banking-fill)" stroke="#3a3f48" stroke-width="2">BANKING</text>
  </svg>

  <p class="subtitle">The Who's What's and How's of Internet Banking</p>

  <div class="banknotes" role="img" aria-label="Photograph of assorted banknotes from many countries spread across each other"></div>

  <p class="tagline">A PRACTICAL GUIDE TO<br>ANSWER ALL YOUR QUESTIONS</p>

  <p class="author">By: Colin Pettifer</p>
</div>
</body>
</html>
```